Roofing Company needs Business card design

We need a business card design for our roofing contracting company. We do Residential and commercial roofing. Design need to be modern, professional and clean. The design should communicate quality and professionalism. We would like to have rounded corners, but open to your ideas.
Company Name: Kestrel roofing Solutions
Company Address: (dummy text)
Name on business card: (dummy text)
And following lines:
Storm damage specialists
commercial & residential
shingles, flat and metal roofs./
Open to background colors.
I have ai. and eps files of logo if needed.
just let me know.
Mostly residential customers but we do commercial too.
Roofing

```html
<!DOCTYPE html>
<html lang="en">
<head>
<meta charset="utf-8">
<title>Kestrel roofing Solutions – Business Card</title>
<link rel="stylesheet" href="https://fonts.googleapis.com/css2?family=Arimo:wght@400;700&display=swap">
<style>
  :root {
    --stage: #000000;
    --card: #8c8c8c;
    --card-edge: #a3a3a3;
    --ink: #1c1c1c;
    --ink-soft: #262626;
    --divider-dark: #3a3a3a;
    --divider-light: #b0b0b0;
  }
  * { margin: 0; padding: 0; box-sizing: border-box; }
  html, body {
    width: 1200px;
    height: 375px;
    overflow: hidden;
    background: var(--stage);
    font-family: "Arimo", Arial, sans-serif;
  }
  .canvas {
    position: relative;
    width: 1200px;
    height: 375px;
  }
  .card {
    position: absolute;
    top: 35px;
    width: 559px;
    height: 303px;
    border-radius: 12px;
    background: linear-gradient(180deg, var(--card-edge) 0%, var(--card) 18%, var(--card) 100%);
    overflow: hidden;
  }
  .card--front { left: 29px; }
  .card--back { left: 610px; }

  .front-brand {
    position: absolute;
    left: 0;
    right: 0;
    top: 0;
    bottom: 0;
    display: flex;
    align-items: center;
    justify-content: center;
  }
  .brand-name {
    font-weight: 700;
    color: var(--ink);
    font-size: 36px;
    letter-spacing: 0.5px;
  }

  .services {
    position: absolute;
    left: 0;
    width: 296px;
    top: 0;
    height: 100%;
    text-align: center;
  }
  .services li {
    list-style: none;
    position: absolute;
    left: 0;
    right: 0;
    font-weight: 700;
    font-size: 19px;
    color: var(--ink);
  }
  .services li:nth-child(1) { top: 27px; }
  .services li:nth-child(2) { top: 77px; }
  .services li:nth-child(3) { top: 126px; }
  .services li:nth-child(4) { top: 174px; }

  .back-brand {
    position: absolute;
    left: 0;
    width: 296px;
    top: 254px;
    text-align: center;
    font-weight: 700;
    font-size: 15px;
    color: var(--ink);
  }

  .divider {
    position: absolute;
    left: 296px;
    top: 0;
    width: 3px;
    height: 100%;
    border-left: 2px solid var(--divider-dark);
    border-right: 1px solid var(--divider-light);
  }

  .contact {
    position: absolute;
    right: 23px;
    top: 0;
    height: 100%;
    text-align: right;
    color: var(--ink-soft);
  }
  .contact .employee-name {
    position: absolute;
    right: 0;
    top: 26px;
    white-space: nowrap;
    font-weight: 700;
    font-size: 21px;
    letter-spacing: 0.4px;
  }
  .contact .employee-title {
    position: absolute;
    right: 0;
    top: 55px;
    white-space: nowrap;
    font-style: italic;
    font-size: 19px;
  }
  .contact .phone {
    position: absolute;
    right: 0;
    top: 159px;
    white-space: nowrap;
    font-size: 25px;
    letter-spacing: 0.5px;
  }
  .contact .address {
    position: absolute;
    right: 0;
    top: 247px;
    white-space: nowrap;
    font-style: normal;
    font-size: 18px;
    line-height: 22px;
    letter-spacing: 0.3px;
  }
</style>
</head>
<body>
<main class="canvas">
  <section class="card card--front" aria-label="Card front">
    <div class="front-brand">
      <span class="brand-name">Kestrel roofing Solutions</span>
    </div>
  </section>

  <section class="card card--back" aria-label="Card back">
    <ul class="services">
      <li>storm damage specialists</li>
      <li>commercial &amp; residential</li>
      <li>shingles</li>
      <li>flat and metal roofs</li>
    </ul>
    <div class="back-brand">Kestrel roofing Solutions</div>

    <div class="divider"></div>

    <div class="contact">
      <p class="employee-name">Employee Name</p>
      <p class="employee-title">Title</p>
      <p class="phone">(555) 555-5555</p>
      <address class="address">123 Some Street<br>Somewhere, AA 12345</address>
    </div>
  </section>
</main>
</body>
</html>
```